Communication Skill: GLOW Bridge

I need a Design for a skill I teach to youth. That's why the title GLOW Bridge. GLOW stands for Thoughts, Emotions, Concerns, Hopes & Desires. Under each word are some examples that are meant to help people discuss certain things. I tried to create something myself but want something much more creative and dynamic. I have attached what I designed because it has the information I need in the design. Want it to have a techie look to it.

```html
<!DOCTYPE html>
<html lang="en">
<head>
<meta charset="utf-8">
<title>GLOW Bridge</title>
<link rel="stylesheet" href="https://fonts.googleapis.com/css2?family=Domine:wght@700&family=Open+Sans:wght@500;700&family=Zilla+Slab:wght@700&display=swap">
<style>
  :root {
    --ink: #231f20;
    --title: #3b3026;
    --bg: #ffffff;
    --orange-a: #fdb913;
    --orange-b: #ef5a24;
    --purple-a: #95268b;
    --purple-b: #d0569c;
    --green-a: #a9cd3a;
    --green-b: #e2e52a;
    --teal-a: #86c4ae;
    --teal-b: #138ec6;
    --disc-a: #ffffff;
    --disc-b: #d4d6d9;
    --letter-t: #ee7d22;
    --letter-e: #d51f8a;
    --letter-c: #7ab317;
    --letter-h: #17a7ad;
  }
  * { box-sizing: border-box; margin: 0; padding: 0; }
  html, body { width: 1200px; height: 1080px; overflow: hidden; background: var(--bg); }
  .canvas { position: relative; width: 1200px; height: 1080px; background: var(--bg); }
  .title {
    position: absolute; top: 58px; left: 0; width: 100%;
    text-align: center;
    font-family: "Domine", Georgia, serif; font-weight: 700;
    font-size: 72px; letter-spacing: 2px; color: var(--title);
  }
  .petal {
    position: absolute; width: 408px; height: 408px;
    box-shadow: 0 6px 18px rgba(0,0,0,0.12);
  }
  .petal--thoughts { left: 180px; top: 180px; border-radius: 50% 50% 0 50%;
    background: linear-gradient(135deg, var(--orange-a), var(--orange-b)); }
  .petal--emotions { left: 612px; top: 180px; border-radius: 50% 50% 50% 0;
    background: linear-gradient(200deg, var(--purple-a), var(--purple-b)); }
  .petal--concerns { left: 180px; top: 612px; border-radius: 50% 0 50% 50%;
    background: linear-gradient(135deg, var(--green-a), var(--green-b)); }
  .petal--hopes { left: 612px; top: 612px; border-radius: 0 50% 50% 50%;
    background: linear-gradient(135deg, var(--teal-a), var(--teal-b)); }
  .disc {
    position: absolute; left: 34px; top: 34px; width: 340px; height: 340px;
    border-radius: 50%;
    border: 4px solid #fff;
    background: radial-gradient(circle at 40% 30%, var(--disc-a), var(--disc-b) 85%);
    box-shadow: 0 6px 16px rgba(0,0,0,0.25);
    display: flex; flex-direction: column; align-items: center;
    padding-top: 28px; text-align: center; color: var(--ink);
  }
  .initial {
    font-family: "Zilla Slab", Georgia, serif; font-weight: 700;
    font-size: 96px; line-height: 1;
  }
  .initial--t { color: var(--letter-t); }
  .initial--e { color: var(--letter-e); }
  .initial--c { color: var(--letter-c); }
  .initial--h { color: var(--letter-h); }
  .word {
    font-family: "Open Sans", Arial, sans-serif; font-weight: 700;
    font-size: 38px; line-height: 1.1; margin-top: 4px; letter-spacing: 0.5px;
  }
  .prompts {
    font-family: "Open Sans", Arial, sans-serif; font-weight: 500;
    font-size: 19.5px; line-height: 1.38; margin-top: 6px; white-space: pre;
  }
  .icon { position: absolute; width: 66px; height: 66px; }
  .icon--cloud { left: 352px; top: 350px; }
  .icon--mood { left: 38px; top: 350px; }
  .icon--worry { left: 348px; top: 22px; }
  .icon--star { left: 30px; top: 22px; }
</style>
</head>
<body>
<main class="canvas">
  <h1 class="title">GLOW BRIDGE</h1>

  <section class="petal petal--thoughts">
    <div class="disc">
      <span class="initial initial--t">T</span>
      <h2 class="word">THOUGHTS</h2>
      <p class="prompts">It seems…  I wonder…
It’s my opinion… I believe…
I assume… I think…</p>
    </div>
    <svg class="icon icon--cloud" viewBox="0 0 66 66" aria-hidden="true">
      <path d="M14 40a10 10 0 0 1 4-19 13 13 0 0 1 24-4 11 11 0 0 1 16 10 8 8 0 0 1-4 13z" fill="#fff"/>
      <circle cx="20" cy="50" r="5" fill="#fff"/>
      <circle cx="13" cy="59" r="3" fill="#fff"/>
    </svg>
  </section>

  <section class="petal petal--emotions">
    <div class="disc">
      <span class="initial initial--e">E</span>
      <h2 class="word">EMOTIONS</h2>
      <p class="prompts">I’m…  hopeful  worried  sad
afraid  mad  glad happy
confident insecure  lonely
bothered  uncertain</p>
    </div>
    <svg class="icon icon--mood" viewBox="0 0 66 66" role="img" aria-label="Mood icon">
      <circle cx="33" cy="33" r="29" fill="none" stroke="#fff" stroke-width="4"/>
    </svg>
  </section>

  <section class="petal petal--concerns">
    <div class="disc">
      <span class="initial initial--c">C</span>
      <h2 class="word">CONCERNS</h2>
      <p class="prompts">I worry about…
I’m afraid that…
I’m nervous because…
It bothers me that…</p>
    </div>
    <svg class="icon icon--worry" viewBox="0 0 66 66" role="img" aria-label="Worry icon">
      <circle cx="33" cy="33" r="31" fill="#fff"/>
    </svg>
  </section>

  <section class="petal petal--hopes">
    <div class="disc">
      <span class="initial initial--h">H</span>
      <h2 class="word">HOPES</h2>
      <p class="prompts">I hope…  I wish…
It’s my desire…
I’d like to see…
I want…  I need…</p>
    </div>
    <svg class="icon icon--star" viewBox="0 0 66 66" aria-hidden="true">
      <path d="M33 6l8 17 18 2-13 13 4 19-17-9-17 9 4-19L7 25l18-2z" fill="#fff"/>
    </svg>
  </section>
</main>
</body>
</html>
```